New design for existing catalog pages

We want to update and improve our existing design. The existing products on the designs should be adopted. Also the prices, descriptions and article numbers.
It is important that we receive an Indesign file that we can adapt. Also replace the images and adjust texts and prices.

Target Market(s)

Older people with high incomes. More conservative people.

Industry/Entity Type

Münzen und Briefmarkenhandel

Requirements
Must have
• Noble, simple and timeless design that looks high quality.
Nice to have
• The expensive products should be presented accordingly
Should not have
• Don't look cheap. Not too many different and bright colors

```html
<!DOCTYPE html>
<html lang="de">
<head>
<meta charset="utf-8">
<title>Katalog – Top Münz-Raritäten &amp; Helvetische Republik</title>
<link rel="stylesheet" href="https://fonts.googleapis.com/css2?family=Outfit:wght@300;400;500;600;700&display=swap">
<style>
  :root{
    --navy:#22399a;
    --ink:#111319;
    --text:#2b2e36;
    --panel:#eceef5;
    --paper:#ffffff;
    --bg:#dfe3ea;
  }
  *{box-sizing:border-box;margin:0;padding:0}
  html,body{width:1200px;height:1200px;overflow:hidden;background:linear-gradient(135deg,#f4f6f9 0%,#d5dae3 60%,#dfe3ea 100%);font-family:'Outfit',sans-serif;color:var(--text)}
  .spread{position:absolute;left:60px;top:224px;width:1738px;height:1210px;transform:scale(0.6211);transform-origin:0 0}
  .page{position:absolute;top:0;width:857px;height:1210px;background:var(--paper);box-shadow:0 12px 30px rgba(30,40,70,.18);overflow:hidden}
  .page--left{left:0}
  .page--right{left:881px}
  .abs{position:absolute}
  .page-title{font-weight:700;font-size:44px;line-height:52px;color:var(--navy);white-space:nowrap}
  .rule{position:absolute;height:2px;background:var(--navy)}
  .rule--thin{height:1.5px}
  .item-title{font-weight:500;font-size:25px;line-height:30px;color:var(--ink);white-space:nowrap}
  .item-title .hl{color:var(--navy)}
  .heading-row{position:absolute;display:flex;align-items:center;gap:14px}
  .facts{list-style:none;font-size:14px;font-weight:500;color:var(--ink);line-height:24px;white-space:nowrap}
  .facts li{position:relative;padding-left:21px}
  .facts li::before{content:"";position:absolute;left:0;top:12px;width:13px;height:1.5px;background:var(--navy)}
  .facts li::after{content:"";position:absolute;left:7px;top:9px;width:5px;height:5px;border-top:1.5px solid var(--navy);border-right:1.5px solid var(--navy);transform:rotate(45deg)}
  .copy{font-size:14px;font-weight:300;line-height:23px;color:var(--text)}
  .panel{position:absolute;background:var(--panel)}
  .sku{position:absolute;font-size:15px;line-height:18px;font-weight:500;color:var(--ink)}
  .price{position:absolute;font-size:15px;line-height:18px;font-weight:500;color:var(--navy);text-align:right}
  .badge{display:inline-flex;align-items:center;gap:5px;height:20px;padding:0 6px 0 3px;background:var(--navy);color:#fff;font-size:13px;font-weight:600;letter-spacing:.3px;white-space:nowrap}
  .badge--abs{position:absolute}
  .badge svg{background:#fff;width:18px;height:15px;padding:1px}
  .coin{position:absolute;overflow:visible}
  .pattern{position:absolute;left:0;right:0;top:1050px;bottom:0;background:linear-gradient(#fff,#f2f3f7)}
  .folio{position:absolute;top:1143px;width:40px;height:36px;background:var(--navy);color:#fff;font-size:14px;display:flex;align-items:center;justify-content:center}
  .running{position:absolute;top:1152px;font-size:14px;line-height:18px;font-weight:300;color:var(--ink);white-space:nowrap}
  .offer-name{position:absolute;font-size:15px;line-height:18px;font-weight:600;color:var(--ink);white-space:nowrap}
</style>
</head>
<body>
<svg width="0" height="0" style="position:absolute">
  <defs>
    <radialGradient id="gold" cx="38%" cy="35%" r="70%">
      <stop offset="0" stop-color="#fbeaa0"/>
      <stop offset=".55" stop-color="#e2c158"/>
      <stop offset="1" stop-color="#a98423"/>
    </radialGradient>
    <radialGradient id="goldPale" cx="38%" cy="35%" r="70%">
      <stop offset="0" stop-color="#fff6d6"/>
      <stop offset=".6" stop-color="#ebd592"/>
      <stop offset="1" stop-color="#b99a4a"/>
    </radialGradient>
  </defs>
</svg>

<div class="spread">
  <!-- Page 13 -->
  <section class="page page--left">
    <div class="pattern"></div>
    <h1 class="page-title abs" style="left:55px;top:40px">Top<br>Münz-Raritäten</h1>
    <div class="rule" style="left:393px;top:121px;width:412px"></div>

    <h2 class="item-title abs" style="left:55px;top:172px">20 Franken 1873,<br><span class="hl">3-Punkt Probeprägung</span></h2>
    <ul class="facts abs" style="left:55px;top:246px">
      <li>Jahr 1873</li><li>Gold – 900/1'000 Feinheit</li><li>Gewicht 6,451 Gramm</li>
    </ul>
    <ul class="facts abs" style="left:250px;top:246px">
      <li>Durchmesser 21mm</li><li>Auflage: 1'000 Stück</li>
    </ul>
    <div class="abs" style="left:55px;top:329px;width:344px;border-top:1.5px dashed var(--navy)"></div>
    <p class="copy abs" style="left:55px;top:341px;width:345px">1873 liess das Finanzdepartement vom bekannten Graveur Ludwig Werner in seiner Prägestätte in Brüssel ein Stempelpaar und 1'000 Exemplare einer neuen Eidgenössischen Goldmünze anfertigen.</p>

    <div class="panel" style="left:448px;top:172px;width:357px;height:251px"></div>
    <svg class="coin" role="img" aria-label="Goldmünze 20 Franken 1873, Wertseite und sitzende Helvetia" style="left:430px;top:150px" width="400" height="250" viewBox="0 0 400 250">
      <circle cx="98" cy="104" r="95" fill="url(#gold)"/>
      <circle cx="281" cy="129" r="108" fill="url(#gold)" stroke="#b08a2a" stroke-width="2"/>
    </svg>
    <div class="sku" style="left:464px;top:398px">7870.1873.01</div>
    <div class="price" style="right:68px;top:398px">9995,– CHF</div>

    <p class="copy abs" style="left:55px;top:438px;width:740px">Der oberste der drei Punkte beinhaltete das Münzzeichen des Graveurs und stellte einen Engelskopf dar, der jedoch bei oberflächlicher Betrachtung als Punkt wahrgenommen wird.</p>
    <div class="rule rule--thin" style="left:55px;top:500px;width:732px"></div>

    <div class="heading-row" style="left:55px;top:520px">
      <h2 class="item-title"><span class="hl">Das 100 Franken Vreneli</span> von 1925</h2>
      <span class="badge"><svg viewBox="0 0 18 16"><path d="M4 2h10l3 4-8 9-8-9z M1 6h16 M7 2l2 13 2-13" fill="none" stroke="#22399a" stroke-width="1.2"/></svg>TOP - RARITÄT</span>
    </div>
    <div class="panel" style="left:55px;top:577px;width:330px;height:209px"></div>
    <svg class="coin" role="img" aria-label="Goldmünze 100 Franken 1925, Wertseite und Helvetiakopf" style="left:49px;top:567px" width="360" height="180" viewBox="0 0 360 180">
      <circle cx="87" cy="87" r="87" fill="url(#goldPale)"/>
      <circle cx="270" cy="87" r="87" fill="url(#goldPale)"/>
    </svg>
    <div class="sku" style="left:65px;top:759px">7874.1925.08</div>
    <div class="price" style="right:482px;top:759px">25900,– CHF</div>
    <p class="copy abs" style="left:448px;top:597px;width:355px">1925, 100 Fr. Gold-Vreneli, bis unzirkuliert, mit Stempelglanz, Top-Erhaltung, Durchmesser: 35mm, Motiv: Helvetiakopf (Vreneli), Entwurf: Félix Ulric Lambert, Neuchâtel, Münzzeichen B, Auflage: 5'000</p>

    <div class="rule rule--thin" style="left:55px;top:810px;width:732px"></div>
    <div class="heading-row" style="left:55px;top:827px">
      <h2 class="item-title"><span class="hl">Das 100 Franken Vreneli</span> von 1925</h2>
      <span class="badge"><svg viewBox="0 0 18 16"><path d="M9 1.5l2.2 4.6 5 .6-3.7 3.4 1 5-4.5-2.5-4.5 2.5 1-5L1.8 6.7l5-.6z" fill="none" stroke="#22399a" stroke-width="1.2"/></svg>TOP - QUALITÄT</span>
    </div>
    <p class="copy abs" style="left:55px;top:904px;width:345px">1925, 100 Fr. Gold-Vreneli, fast FDC, Top-Erhaltung, Durchmesser: 35mm, Motiv: Helvetiakopf (Vreneli), Entwurf: Félix Ulric Lambert, Neuchâtel, Münzzeichen B, Auflage: 5'000</p>
    <div class="panel" style="left:467px;top:884px;width:329px;height:208px"></div>
    <svg class="coin" role="img" aria-label="Goldmünze 100 Franken 1925, Wertseite und Helvetiakopf" style="left:461px;top:872px" width="360" height="180" viewBox="0 0 360 180">
      <circle cx="87" cy="87" r="87" fill="url(#goldPale)"/>
      <circle cx="269" cy="87" r="87" fill="url(#goldPale)"/>
    </svg>
    <div class="sku" style="left:476px;top:1066px">7874.1925.07</div>
    <div class="price" style="right:71px;top:1066px">25900,– CHF</div>

    <div class="folio" style="left:53px">13</div>
    <div class="running" style="left:104px">Top Münz-Raritäten</div>
    <div class="rule" style="left:240px;top:1162px;width:565px;height:1px"></div>
  </section>

  <!-- Page 14 -->
  <section class="page page--right">
    <div class="pattern"></div>
    <h1 class="page-title abs" style="right:54px;top:40px;text-align:right">Helvetische<br>Republik - Duplonen</h1>
    <div class="rule" style="left:52px;top:121px;width:330px"></div>

    <h2 class="item-title abs" style="left:52px;top:159px"><span class="hl">Duplone und Doppelduplone</span> der Helvetischen Republik 1798 - 1803</h2>
    <p class="copy abs" style="left:52px;top:207px;width:492px">Helvetische Republik ist die offizielle Bezeichnung des schweizerischen Staatswesens, das am 12. April 1798 die alte Eidgenossenschaft ablöste und bis zum 10. März 1803 bestand. Frankreich nutzte die bestehende Unzufriedenheit der ländlichen Eliten in den Untertanengebieten der alten Eidgenossenschaft, sowie der aufgeklärten Bürger in den städtischen Orten und förderte gezielt revolutionäre Bestrebungen. Angefacht oder ausgelöst und zugleich auch abgesichert wurde die Umwälzung durch französische Truppen, die ab Ende Januar in einer Zangenbewegung von der Waadt und vom Jura her in das westliche Mittelland vorstiessen (Franzoseneinfall). In den Kampfhandlungen Anfang März 1798 ging die alte Eidgenossenschaft unter.</p>
    <div class="abs" style="left:568px;top:216px;width:2px;height:220px;background:var(--navy)"></div>
    <ul class="facts abs" style="left:593px;top:216px;width:230px;line-height:20px;white-space:normal">
      <li style="margin-bottom:5px">Schweiz - 16 / 32 Franken</li>
      <li style="margin-bottom:5px">1800, Helvetische Republik</li>
      <li style="margin-bottom:5px">7,65 Gramm / 15,26<br>Gramm - Gold</li>
      <li style="margin-bottom:5px">23 mm / 29 mm Durchmesser</li>
      <li>vorzüglich bis unzirkuliert</li>
    </ul>
    <p class="copy abs" style="left:52px;top:448px;width:745px">Einige Städte, allen voran Bern, hatten beträchtliche Vermögen in ihren Schatzkammern. Der sogenannte Staatsschatz von Bern wurde von den Französischen Truppen geplündert. Mehrere Kutschen mit Gold und Silber, sowie die Bären aus dem Bärengraben, wurden nach Paris gekarrt. Mit der Einführung der Helvetischen Republik ging das Münzwesen von den Kantonen auf den Zentralstaat über und der Franken wurde als Währung festgelegt. In dieser Zeit entstanden die Duplonen (16 Franken) und Doppelduplonen (32 Franken) der Helvetischen Republik.</p>

    <div class="panel" style="left:52px;top:660px;width:752px;height:442px"></div>
    <svg class="coin" role="img" aria-label="Goldmünzen der Helvetischen Republik 1800: Doppelduplone 32 Franken beidseitig und Duplone 16 Franken" style="left:0;top:560px" width="700" height="560" viewBox="0 0 700 560">
      <circle cx="390" cy="174" r="148" fill="url(#gold)"/>
      <circle cx="252" cy="389" r="167" fill="url(#gold)" stroke="#9c7a1c" stroke-width="2"/>
      <circle cx="558" cy="267" r="106" fill="url(#goldPale)"/>
    </svg>
    <span class="badge badge--abs" style="left:120px;top:710px"><svg viewBox="0 0 18 16"><path d="M4 2h10l3 4-8 9-8-9z M1 6h16 M7 2l2 13 2-13" fill="none" stroke="#22399a" stroke-width="1.2"/></svg>TOP - RARITÄT</span>
    <span class="badge badge--abs" style="left:490px;top:932px"><svg viewBox="0 0 18 16"><circle cx="7" cy="8" r="5.5" fill="none" stroke="#22399a" stroke-width="1.2"/><circle cx="11" cy="8" r="5.5" fill="none" stroke="#22399a" stroke-width="1.2"/></svg>DUPLONENPAAR</span>

    <div class="offer-name" style="left:427px;top:985px">Helvetische Republik - Duplone 16 Franken</div>
    <div class="sku" style="left:427px;top:1011px">7997.1800.015</div>
    <div class="price" style="right:73px;top:1011px">9500,– CHF</div>
    <div class="offer-name" style="left:427px;top:1040px">Helvetische Republik - Doppelduplone 32 Franken</div>
    <div class="sku" style="left:427px;top:1065px">7997.1800.025</div>
    <div class="price" style="right:73px;top:1065px">28900,– CHF</div>

    <div class="rule" style="left:52px;top:1162px;width:490px;height:1px"></div>
    <div class="running" style="right:104px">Helvetische Republik - Duplonen</div>
    <div class="folio" style="left:764px">14</div>
  </section>
</div>
</body>
</html>
```